my website is toncielbrode.com. (brand name is ton ciel brodé) This is just a template that i have choose for. The content and the pictures are not about my business just the template.
I would like to have 4 pages for now. 1 homepage, which will be an overview for all pages, it is right now in this way. It will directly highlight my story. My website will tell an exclusive story about details which makes the difference and will make people happy with very small things. It will be art related but very stylish as well. I also want to have a event agenda on my homepage where people can see where my next event is. Page 2 my blog, where I will write weekly about mindset, lifestyle and details. Inspiration place for people who are looking for unique and exclusive approaches in life. Page 3 shop, where I will sell my stuff which is handmade and unique, it will be limited edition stuff. Mostly I will make the designs from marbling art, which I am a teacher for. (https://www.vidorama-example.com/watch?v=Xk3pQr7LmZa) check this video out for more. Page 4 is book page. Here people will be able to book private or group classes for marbling art (check the video). I have already a community of more than 500 people on join nest, which will be my public as well. I wanna implement the join nest button on this page as well. to be able to track.

This is about my website. I also need a logo for my brand, which will suit my website and my goals.

I can also give you a reference website, which really like as structure and style;
https://www.brightmorrowgoods-example.com/products/the-quiet-ledger?gclid=Zx8RtYpWq2LmN4vBcD6sKjH3gFaE9uIoP1lKzXcVbNm7QwErTyUiOp0AsDfGhJkLzXcVbNm5Qw2ErTyUi_oPaSd8FgHjKlZxC_vbNQ

ton ciel brodé

4 page

• I can also give you a reference website, which really like as structure and style;
• https://www.brightmorrowgoods-example.com/products/the-quiet-ledger?gclid=Zx8RtYpWq2LmN4vBcD6sKjH3gFaE9uIoP1lKzXcVbNm7QwErTyUiOp0AsDfGhJkLzXcVbNm5Qw2ErTyUi_oPaSd8FgHjKlZxC_vbNQ

```html
<!DOCTYPE html>
<html lang="en">
<head>
<meta charset="utf-8">
<title>ton ciel brodé — Home</title>
<link rel="stylesheet" href="https://fonts.googleapis.com/css2?family=Oswald:wght@300;400;500&display=swap">
<style>
:root{
  --ink:#000;
  --paper:#fff;
  --heading:#2b2b2b;
  --muted:#555;
  --rule:#777;
  --dot:#bdbdbd;
  --label:#d8d8d8;
  --footer-text:#bbb;
  --footer-brand:#ddd;
  --footer-rule:#555;
  --legal:#888;
  --hero-a:#b89a9e;
  --hero-b:#d9bfc2;
  --hero-c:#9c8488;
}
*{margin:0;padding:0;box-sizing:border-box}
html,body{width:1200px;height:2180px;overflow:hidden;background:var(--paper)}
body{font-family:"Oswald",sans-serif;color:var(--heading);position:relative}
a{text-decoration:none;color:inherit}
.abs{position:absolute}

/* top bar */
.topbar{left:0;top:0;width:1200px;height:33px;background:var(--ink);color:var(--paper);font-size:11px;font-weight:300}
.topbar .phone{left:932px;top:9px;display:flex;align-items:center;gap:8px}
.topbar .call{left:1032px;top:9px}
.topbar .divider{left:1076px;top:6px;width:1px;height:20px;background:var(--paper)}
.topbar .social{top:9px;width:15px;height:15px;border:1.5px solid var(--paper);border-radius:50%}

/* nav */
.nav{left:0;top:33px;width:1200px;height:71px;font-size:16px}
.nav a{color:var(--heading);position:absolute;top:28px;line-height:20px}
.nav .brand{font-size:24px;top:22px;line-height:28px}
.nav .current::after{content:"";position:absolute;left:-17px;right:-17px;bottom:-4px;height:2px;background:var(--heading)}

/* hero */
.hero{left:0;top:104px;width:1200px;height:474px;background:radial-gradient(circle at 30% 40%,var(--hero-b),var(--hero-a) 60%,var(--hero-c))}
.hero .backdrop{position:absolute;inset:0}
.hero h1{position:absolute;left:0;width:1200px;top:44px;text-align:center;font-size:60px;line-height:76px;font-weight:500;color:var(--heading)}
.hero p{position:absolute;left:285px;width:630px;top:150px;text-align:center;font-size:14px;font-weight:300;line-height:19px;color:var(--heading)}
.hero .cta{position:absolute;left:491px;top:244px;width:218px;height:87px;background:var(--ink);color:var(--paper);font-size:29px;display:flex;align-items:center;justify-content:center}
.hero .arrow{position:absolute;top:222px}
.hero .dots{position:absolute;left:490px;top:428px;display:flex;gap:13px}
.hero .dots span{width:20px;height:20px;border-radius:50%;background:rgba(255,255,255,.45)}
.hero .dots span.on{background:var(--paper)}

/* bands */
.band{left:0;width:1200px;height:131px;background:var(--ink);color:var(--paper)}
.band .btn{position:absolute;left:132px;top:29px;width:218px;height:71px;background:var(--paper);color:var(--ink);font-size:29px;display:flex;align-items:center;justify-content:center}
.band p{position:absolute;left:369px;top:41px;width:736px;font-size:16px;font-weight:500;line-height:22px}

/* shop */
.shop-title{left:0;width:1200px;top:730px;text-align:center;font-size:64px;line-height:84px;font-weight:500}
.product{top:840px;width:284px;height:258px;border:7px solid var(--ink)}
.buy{top:1117px;width:142px;height:41px;background:var(--ink);color:var(--paper);font-size:20px;display:flex;align-items:center;justify-content:center}
.pager{left:523px;top:1203px;display:flex;gap:13px}
.pager span{width:20px;height:20px;border-radius:50%;background:var(--dot);color:var(--paper);font-size:11px;display:flex;align-items:center;justify-content:center}
.pager span.on{background:var(--ink)}

/* contact */
.contact-title{left:0;width:1200px;top:1414px;text-align:center;font-size:38px;line-height:52px;font-weight:500;color:var(--ink)}
.contact-intro{left:0;width:1200px;top:1477px;text-align:center;font-size:15px;font-weight:300;color:var(--muted)}
.info{left:0;width:1200px;display:flex;justify-content:center;align-items:center;gap:8px;font-size:16px;line-height:20px;font-weight:300;color:var(--muted)}
.field-label{left:423px;font-size:16px;color:var(--label);font-weight:300}
.field-hint{left:423px;font-size:13px;color:var(--ink)}
.field-line{left:423px;width:398px;height:2px;background:var(--rule)}
.send{left:498px;top:1925px;width:235px;height:42px;background:var(--ink);color:var(--paper);font-size:22px;font-weight:500;display:flex;align-items:center;justify-content:center}

/* footer */
.footer{left:0;top:2024px;width:1200px;height:156px;background:var(--ink);color:var(--footer-text)}
.footer .link{position:absolute;top:30px;font-size:16px;line-height:20px}
.footer .brand{position:absolute;top:24px;font-size:24px;line-height:30px;color:var(--footer-brand)}
.footer .rule{position:absolute;height:1px;background:var(--footer-rule)}
.footer .social{position:absolute;top:96px;width:15px;height:15px;border-radius:50%;background:var(--paper)}
.footer .legal{position:absolute;left:0;width:1200px;top:137px;text-align:center;font-size:8px;color:var(--legal)}
</style>
</head>
<body>

<header class="abs topbar">
  <div class="abs phone">
    <svg width="10" height="10" viewBox="0 0 24 24"><path fill="#fff" d="M6.6 10.8a15 15 0 0 0 6.6 6.6l2.2-2.2a1 1 0 0 1 1-.25 11.4 11.4 0 0 0 3.6.6 1 1 0 0 1 1 1V20a1 1 0 0 1-1 1A17 17 0 0 1 3 4a1 1 0 0 1 1-1h3.5a1 1 0 0 1 1 1c0 1.25.2 2.45.6 3.6a1 1 0 0 1-.25 1z"/></svg>
    <span>1-555-014-2270</span>
  </div>
  <span class="abs call">Call Us!</span>
  <span class="abs divider"></span>
  <span class="abs social" style="left:1095px"></span>
  <span class="abs social" style="left:1120px"></span>
</header>

<nav class="abs nav">
  <a href="#" class="current" style="left:393px">Home</a>
  <a href="#" style="left:469px">Blog</a>
  <a href="#" class="brand" style="left:538px">ton ciel brodé</a>
  <a href="#" style="left:706px">Shop</a>
  <a href="#" style="left:777px">Book</a>
</nav>

<section class="abs hero">
  <div class="backdrop" role="img" aria-label="Close-up of a stylus drawn through pink and grey marbling paint"></div>
  <h1>Happiness Lives In Details</h1>
  <p>ton ciel brodé tells the story of the small details that make the difference. Handmade, limited edition pieces born from marbling art, where every swirl of colour is unique. Stylish, art-led and made to bring joy in the smallest things. Discover the story, the pieces and the next event today.</p>
  <a href="#" class="cta">Shop Now</a>
  <svg class="arrow" style="left:7px" width="34" height="34" viewBox="0 0 34 34"><circle cx="17" cy="17" r="15" fill="none" stroke="#fff" stroke-width="2"/><path d="M20 10l-7 7 7 7" fill="none" stroke="#fff" stroke-width="2.5"/></svg>
  <svg class="arrow" style="left:1159px" width="34" height="34" viewBox="0 0 34 34"><circle cx="17" cy="17" r="15" fill="none" stroke="#fff" stroke-width="2"/><path d="M14 10l7 7-7 7" fill="none" stroke="#fff" stroke-width="2.5"/></svg>
  <div class="dots"><span class="on"></span><span></span><span></span><span></span><span></span><span></span><span></span></div>
</section>

<section class="abs band" style="top:578px">
  <a href="#" class="btn">Go To Blog</a>
  <p>A new story every week on mindset, lifestyle and details. An inspiration place for anyone looking for unique and exclusive approaches in life, and for the small things that quietly make people happy.</p>
</section>

<h2 class="abs shop-title">SHOP</h2>

<div class="abs product" style="left:93px;background:linear-gradient(160deg,#6b4a3a,#8a5a45 55%,#a8b8a0)" role="img" aria-label="Marbling tray with paint bottles and swirled brown and green pattern"></div>
<div class="abs product" style="left:458px;background:linear-gradient(160deg,#5a4a44,#2a2624 55%,#4a4440)" role="img" aria-label="Dark marbling bath with paint rings and colour bottles"></div>
<div class="abs product" style="left:823px;background:linear-gradient(160deg,#b9433f,#9cc9c8 35%,#8bbfb9 70%,#d6a0a8)" role="img" aria-label="Turquoise marbled paper with pink floral motifs"></div>

<a href="#" class="abs buy" style="left:165px">buy</a>
<a href="#" class="abs buy" style="left:530px">buy</a>
<a href="#" class="abs buy" style="left:895px">buy</a>

<div class="abs pager"><span class="on">1</span><span>2</span><span>3</span><span>4</span><span>5</span></div>

<section class="abs band" style="top:1250px">
  <a href="#" class="btn">Go To Book</a>
  <p>Next event: Saturday 14 June, open marbling workshop in Port Alder. Book a private or group class in marbling art and join our community of more than 500 makers on join nest for every upcoming date.</p>
</section>

<h2 class="abs contact-title">Contact Us</h2>
<p class="abs contact-intro">For general comments and inquiries, please get in touch with us with the form below.</p>

<div class="abs info" style="top:1506px">
  <svg width="13" height="13" viewBox="0 0 24 24"><path fill="#555" d="M6.6 10.8a15 15 0 0 0 6.6 6.6l2.2-2.2a1 1 0 0 1 1-.25 11.4 11.4 0 0 0 3.6.6 1 1 0 0 1 1 1V20a1 1 0 0 1-1 1A17 17 0 0 1 3 4a1 1 0 0 1 1-1h3.5a1 1 0 0 1 1 1c0 1.25.2 2.45.6 3.6a1 1 0 0 1-.25 1z"/></svg>
  <span>0815 550 372</span>
</div>
<div class="abs info" style="top:1526px">
  <svg width="15" height="12" viewBox="0 0 24 18"><rect width="24" height="18" rx="2" fill="#555"/><path d="M1 2l11 8 11-8" fill="none" stroke="#fff" stroke-width="2"/></svg>
  <span>hello@toncielbrode.com</span>
</div>
<div class="abs info" style="top:1546px">
  <svg width="12" height="14" viewBox="0 0 24 28"><path fill="#555" d="M12 0a10 10 0 0 0-10 10c0 7.5 10 18 10 18s10-10.5 10-18A10 10 0 0 0 12 0zm0 14a4 4 0 1 1 0-8 4 4 0 0 1 0 8z"/></svg>
  <span>Port Alder, Elmshire</span>
</div>

<form>
  <span class="abs field-label" style="top:1560px">Name</span>
  <span class="abs field-hint" style="top:1592px">insert your name</span>
  <span class="abs field-line" style="top:1611px"></span>

  <span class="abs field-label" style="top:1635px">Email</span>
  <span class="abs field-hint" style="top:1667px">insert your email address</span>
  <span class="abs field-line" style="top:1686px"></span>

  <span class="abs field-label" style="top:1710px">Subject</span>
  <span class="abs field-hint" style="top:1742px">insert your subject</span>
  <span class="abs field-line" style="top:1761px"></span>

  <span class="abs field-label" style="top:1785px">Message</span>
  <span class="abs field-hint" style="top:1817px">insert your message</span>
  <span class="abs field-line" style="top:1886px"></span>

  <span class="abs send">Send</span>
</form>

<footer class="abs footer">
  <a href="#" class="link" style="left:393px">Home</a>
  <a href="#" class="link" style="left:469px">Blog</a>
  <a href="#" class="brand" style="left:541px">ton ciel brodé</a>
  <a href="#" class="link" style="left:706px">Shop</a>
  <a href="#" class="link" style="left:777px">Book</a>
  <span class="rule" style="left:494px;top:76px;width:212px"></span>
  <span class="social" style="left:532px"></span>
  <span class="social" style="left:587px"></span>
  <span class="social" style="left:641px"></span>
  <span class="rule" style="left:305px;top:131px;width:589px"></span>
  <p class="legal">© All rights reserved · ton ciel brodé</p>
</footer>

</body>
</html>
```